Saving Lives with Dental Sleep Medicine

Looking for a brochure to market Dental Sleep Medicine educational courses . Whoever wins this bid will be hired to design the rest of our marketing campaign.
Design should be clean, simple with a modern feel. Not busy. Our courses utilize the most modern technology available.
Brochure content is attached, if you can't fit it all that is ok, we can tweak the content later. We are more focused on the look and feel of this design.
This brochure is marketing a 2 day course so there needs to be a spot for date, location, time & cost. As well as a notice of where to register VelmoraLearning.com, info@velmoralearning.com or call 1.800.###.#### and registration fees.
Also need a spot for Dr. Pelloquist's bio (attached). It's too long so just leave as much space as you can and we can amend the content.
Thank you so much. Looking forward to your designs. VelmEd Team :-)
Updates
Hello,
We are hoping for a minimalist design. Not busy. Clean and simple. We can reduce and minimize verbiage as needed. Just looking for layout and design.
Target Market(s)
Dentists
Requirements
Must have
- Clean lines, simple feel, minimalist and modern. Same font as logo. Black, white, gray.
Should not have
- Busy look and feel

```html
<!DOCTYPE html>
<html lang="en">
<head>
<meta charset="utf-8">
<title>Saving Lives with Dental Sleep Medicine – Course Brochure</title>
<link href="https://fonts.googleapis.com/css2?family=Montserrat:wght@400;500;600;700;800&family=Mulish:ital,wght@0,400;0,600;0,700;0,800;1,400;1,500&display=swap" rel="stylesheet">
<style>
:root{
  --coral:#f76a78;
  --coral-soft:#f9a0a9;
  --ink:#1e1e22;
  --grey:#5f6064;
  --grey-light:#8a8b8f;
  --backdrop:#b1b1b1;
  --white:#ffffff;
  --circle:#c9c9cb;
}
*{margin:0;padding:0;box-sizing:border-box}
html,body{width:1071px;height:1200px;overflow:hidden}
body{background:var(--backdrop);position:relative;font-family:"Mulish",sans-serif;color:var(--white)}
.page{position:absolute;left:142px;width:787px;height:477px;background:var(--white);overflow:hidden}
.page--outside{top:86px}
.page--inside{top:627px}
.page__art{position:absolute;left:0;top:0;width:787px;height:477px}
.abs{position:absolute}

/* outside */
.bio__title{right:403px;top:27px;font-family:"Mulish",sans-serif;font-weight:800;font-size:17px;color:var(--white)}
.bio__title span{font-weight:500}
.bio__text{left:110px;width:418px;top:52px;font-size:6.6px;line-height:10.95px;text-align:right;padding-left:20px;right:auto}
.bio__text--lead{left:108px;width:279px;top:52px;text-align:right}
.bio__text--more{left:21px;width:318px;top:275px;text-align:left}
.contact__title{left:23px;top:368px;font-family:"Montserrat",sans-serif;font-weight:700;font-size:16.5px;letter-spacing:.3px}
.contact__title span{font-weight:500}
.contact__item{font-family:"Montserrat",sans-serif;font-size:10px;letter-spacing:.6px;display:flex;align-items:center;gap:8px}
.contact__icon{width:18px;height:18px;border-radius:50%;background:var(--coral-soft);display:flex;align-items:center;justify-content:center}
.course__title{right:43px;top:34px;text-align:right;font-family:"Montserrat",sans-serif;font-weight:700;font-size:18px;font-variant:small-caps;letter-spacing:1px;line-height:25px;color:var(--ink)}
.course__title .accent{color:var(--coral)}
.course__length{right:45px;top:89px;font-family:"Mulish",sans-serif;font-style:italic;font-size:14px;color:var(--grey-light);letter-spacing:.5px}
.course__date{right:45px;top:355px;font-family:"Montserrat",sans-serif;font-weight:600;font-size:17px;color:var(--ink);font-variant:small-caps;letter-spacing:.8px}
.course__date b{font-weight:700;font-size:19px}
.course__venue{right:65px;top:397px;text-align:right;font-family:"Montserrat",sans-serif;font-size:8.3px;line-height:11px;color:var(--grey)}
.course__pin{right:42px;top:398px;width:18px;height:18px;border-radius:50%;background:var(--coral);display:flex;align-items:center;justify-content:center}
.course__cost{left:485px;top:436px;font-family:"Montserrat",sans-serif;font-weight:700;font-size:14.5px;color:var(--grey);letter-spacing:.5px}
.brand{left:593px;top:433px;display:flex;align-items:center;gap:6px}
.brand__mark{width:14px;height:14px;background:var(--coral)}
.brand__name{font-family:"Montserrat",sans-serif;font-weight:400;font-size:15.5px;color:var(--grey-light)}

/* inside */
.section-title{font-family:"Mulish",sans-serif;font-weight:800;font-size:14.5px;letter-spacing:.3px}
.title--coral{color:var(--coral)}
.course-name{left:27px;top:43px;width:370px;font-style:italic;font-size:13.3px;line-height:19px;color:var(--grey);letter-spacing:.2px}
.topics__title{right:456px;top:101px;font-family:"Mulish",sans-serif;font-weight:400;font-size:15px;color:var(--coral);letter-spacing:.3px}
.topic{position:absolute;left:0;width:330px;height:30px;font-size:7.9px;line-height:10px;color:var(--ink);font-weight:600}
.topic__left{position:absolute;right:212px;top:50%;transform:translateY(-50%);text-align:right;width:110px}
.topic__right{position:absolute;left:157px;top:50%;transform:translateY(-50%);width:120px}
.topic__badge{position:absolute;left:124px;top:1px;width:28px;height:28px;border-radius:50%;background:var(--coral)}
.topic__badge::before{content:"";position:absolute;left:-2px;top:-2px;width:26px;height:26px;border-radius:50%;background:var(--circle)}
.topic__num{position:absolute;font-family:"Mulish",sans-serif;font-size:10px;font-weight:600;color:var(--white)}
.topic__num--a{left:6px;top:3px}
.topic__num--b{left:13px;top:11px;color:var(--circle)}
.desc__title{right:35px;top:21px;color:var(--white)}
.desc__text{font-size:7.8px;line-height:12.4px;color:var(--white)}
.objectives__title{left:480px;top:327px;color:var(--white)}
.objectives{left:440px;top:351px;width:330px;list-style:none;font-size:7.8px;line-height:10px;color:var(--white)}
.objectives li{margin-bottom:5.6px}
</style>
</head>
<body>

<!-- Outside spread -->
<section class="page page--outside">
  <svg class="page__art" viewBox="0 0 787 477" aria-hidden="false">
    <polygon points="0,0 393,0 492,190 393,477 0,477" fill="var(--coral)"/>
    <polygon role="img" aria-label="Black and white portrait of the course presenter" points="62,85 108,111.5 108,164.5 62,191 16,164.5 16,111.5" fill="#6d6d70"/>
    <polygon role="img" aria-label="Presenter in a blue suit speaking" points="607,112 712,172.5 712,293.5 607,354 502,293.5 502,172.5" fill="#7f8fb4" stroke="#fff" stroke-width="3"/>
    <polygon role="img" aria-label="Dentists photographing a demonstration with their phones" points="514,181 604,233 604,337 514,389 424,337 424,233" fill="#5a4c48" stroke="#fff" stroke-width="3"/>
    <polygon role="img" aria-label="Course attendees gathered in a dental clinic" points="421,252 498,296.5 498,385.5 421,430 344,385.5 344,296.5" fill="#6b5e58" stroke="#fff" stroke-width="3"/>
  </svg>

  <h2 class="abs bio__title">Brief <span>Bio</span></h2>
  <p class="abs bio__text bio__text--lead">Dr. Pelloquist received his Doctor of Dental Surgery (DDS) Degree and Bachelor of Medical Sciences from Northvale University, Canada. He also earned fellowships from the Halden Institute of Facial Aesthetics &amp; the Corvan Institute for Advanced Dental Studies. He then furthered his education and training by completing a Research Fellowship in the area of "Sleep and Dental Sleep Medicine" at Marlow University Hospital. Dr. Pelloquist is a general dentist who maintains a group of private practices with an interest in Dental Sleep Medicine and TMD Management. He is actively involved in clinical research in Dental Sleep Medicine and his research focuses on developing new technologies to improve treatment outcome predictability and patient selection in Oral Appliance Therapy for patients with OSA (i.e. Obstructive Sleep Apnea) and improving clinical workflow efficiencies, utilizing different digital technologies. He is the recipient of the "2012 &amp; 2015 Clinical Research Award" and "2015 Clinical Excellence Award" from the Academy of Dental Sleep Care (ADSC). He has lectured at numerous annual meetings of sleep and orthodontic societies and many more Sleep meetings across North America and Europe.</p>
  <p class="abs bio__text bio__text--more">He is the founder and director of Northvale Dental Sleep Study Club and the Clinical Director at The Quiet Night Centre in Canada. He is also the Chief Dental Officer at Norvane Sleep Technologies, the developer of "SOMNEx TM" Technology. Dr. Pelloquist is a major advocate for the importance of an inter-disciplinary approach to Dental Sleep Medicine which focuses on the collaboration of Sleep Physicians, Sleep Dentists and other healthcare professionals. He has been treating OSA patients for many years and also has trained hundreds of dentists in Dental Sleep Medicine.</p>

  <h2 class="abs contact__title">GET IN <span>TOUCH</span></h2>
  <div class="abs contact__item" style="left:23px;top:313px;margin-top:0;top:313px;display:none"></div>
  <div class="abs contact__item" style="left:23px;top:399px">
    <span class="contact__icon"><svg width="10" height="10" viewBox="0 0 24 24"><path d="M6.6 10.8a15 15 0 0 0 6.6 6.6l2.2-2.2a1 1 0 0 1 1-.25 11.4 11.4 0 0 0 3.6.6 1 1 0 0 1 1 1V20a1 1 0 0 1-1 1A17 17 0 0 1 3 4a1 1 0 0 1 1-1h3.5a1 1 0 0 1 1 1c0 1.25.2 2.45.6 3.6a1 1 0 0 1-.25 1z" fill="#fff"/></svg></span>180055501234
  </div>
  <div class="abs contact__item" style="left:165px;top:399px">
    <span class="contact__icon"><svg width="10" height="10" viewBox="0 0 24 24" fill="none" stroke="#fff" stroke-width="2"><circle cx="12" cy="12" r="9"/><path d="M3 12h18M12 3c3 3 3 15 0 18M12 3c-3 3-3 15 0 18"/></svg></span>www.velmoralearning.com
  </div>
  <div class="abs contact__item" style="left:23px;top:429px">
    <span class="contact__icon"><svg width="10" height="10" viewBox="0 0 24 24" fill="none" stroke="#fff" stroke-width="2"><rect x="3" y="6" width="18" height="12"/><path d="M3 6l9 7 9-7"/></svg></span>info@velmoralearning.com
  </div>

  <h1 class="abs course__title"><span class="accent">Saving Lives with</span> Dental<br>Sleep Medicine</h1>
  <p class="abs course__length">A 2-day course</p>
  <p class="abs course__date"><b>22</b> Sept, 2018</p>
  <p class="abs course__venue">Marla Fenwick, 418-2290 Quillon Street<br>Bexford NH 11620</p>
  <span class="abs course__pin"><svg width="9" height="11" viewBox="0 0 18 22" fill="none" stroke="#fff" stroke-width="2"><path d="M9 21s7-7 7-12A7 7 0 0 0 2 9c0 5 7 12 7 12z"/><circle cx="9" cy="9" r="2.5"/></svg></span>
  <p class="abs course__cost">COST HERE</p>
  <div class="abs brand"><span class="brand__mark"></span><span class="brand__name">VelmoraLearning</span></div>
</section>

<!-- Inside spread -->
<section class="page page--inside">
  <svg class="page__art" viewBox="0 0 787 477">
    <rect x="394" y="0" width="393" height="477" fill="var(--coral)"/>
    <polygon points="276,165 394,97 394,400 276,340" fill="#ececed"/>
    <polygon role="img" aria-label="Presenter in a navy suit gesturing while teaching" points="300,230 395,168 512,236 512,316 395,384 300,326" fill="#3c4156"/>
    <polygon role="img" aria-label="Attendees watching a live clinical demonstration" points="471,18 548,62.5 548,151.5 471,196 394,151.5 394,62.5" fill="#7a6a62" stroke="#fff" stroke-width="3"/>
    <polygon role="img" aria-label="Lecture room with attendees at laptops" points="318,280 392,322.5 392,407.5 318,450 244,407.5 244,322.5" fill="#8a8480" stroke="#fff" stroke-width="3"/>
  </svg>

  <h2 class="abs section-title title--coral" style="left:27px;top:20px">Course Title</h2>
  <p class="abs course-name">Sleep &amp; Airway Management in a Dental Clinic; SOMNEx Plus System &amp; Fully Digital Workflows for OAT</p>
  <h3 class="abs topics__title">Topics Covered</h3>

  <div class="topic" style="top:122px"><span class="topic__left">Fundamentals of Sleep &amp; Sleep Disorders</span><span class="topic__badge"><span class="topic__num topic__num--a">1</span><span class="topic__num topic__num--b">2</span></span><span class="topic__right">Understand Obstructive Sleep Apnea (OSA) &amp; Treatment Options</span></div>
  <div class="topic" style="top:160px"><span class="topic__left">Sleep Testing</span><span class="topic__badge"><span class="topic__num topic__num--a">3</span><span class="topic__num topic__num--b">4</span></span><span class="topic__right">How to Implement an effective Sleep Screening Protocol in a Dental Clinic</span></div>
  <div class="topic" style="top:201px"><span class="topic__left">Appliance Selection</span><span class="topic__badge"><span class="topic__num topic__num--a">5</span><span class="topic__num topic__num--b">6</span></span><span class="topic__right">How to order an appliance for OAT</span></div>
  <div class="topic" style="top:244px"><span class="topic__left">Importance of patient selection</span><span class="topic__badge"><span class="topic__num topic__num--a">7</span><span class="topic__num topic__num--b">8</span></span><span class="topic__right">Overview of SOMNEx Plus System</span></div>
  <div class="topic" style="top:286px"><span class="topic__left">Hands-on workshop for SOMNEx Tray Fitting</span><span class="topic__badge"><span class="topic__num topic__num--a">9</span><span class="topic__num topic__num--b">0</span></span><span class="topic__right">Hands-on workshop for Bite-Registration</span></div>
  <div class="topic" style="top:329px"><span class="topic__left">Fully Digital Workflow for OAT</span><span class="topic__badge"><span class="topic__num topic__num--a">11</span><span class="topic__num topic__num--b">2</span></span><span class="topic__right">Technology &amp; Sleep</span></div>
  <div class="topic" style="top:370px"><span class="topic__left">SOMNEx Plus Case Studies</span><span class="topic__badge"><span class="topic__num topic__num--a">13</span><span class="topic__num topic__num--b">4</span></span><span class="topic__right">Medical Billing for OAT</span></div>
  <div class="topic" style="top:413px"><span class="topic__left">Simple and easy to follow clinical workflow</span><span class="topic__badge"><span class="topic__num topic__num--a">15</span><span class="topic__num topic__num--b">6</span></span><span class="topic__right">How to maximize the utilization of your SOMNEx Plus at your clinic</span></div>

  <h2 class="abs section-title desc__title">Course Description</h2>
  <p class="abs desc__text" style="left:563px;top:46px;width:200px">Dental Sleep Medicine (DSM) has been growing rapidly over the past decade. Despite such growth, Oral Appliance Therapy (OAT) could be challenging in terms of predictability and workflow efficiency, resulting in many clinicians being reluctant to incorporate "Sleep &amp; OAT" into their clinics. However, most of these challenges can now be addressed by utilizing available technologies in healthcare industry; resulting in improved and predictable clinical workflows, patient experience, quality of care and access to care.</p>
  <p class="abs desc__text" style="left:530px;top:189px;width:238px">This program will review the importance of Sleep &amp; Airway Management in comprehensive inter-disciplinary treatment planning and how airway &amp; sleep disorders, if left untreated, could adversely impact the long-term prognosis of dental treatments. It will also provide a practical step-by-step guide for implementing a simple &amp; predictable "Sleep and Airway Management" program; utilizing easy to implement systems, improved patient communication &amp; education through Intraoral scanning, &amp; 3D imaging AND a fully digital workflow for OAT.</p>

  <h2 class="abs section-title objectives__title">Learning Objectives</h2>
  <ul class="abs objectives">
    <li>Step by step instruction on how to systematically integrate sleep into your practice</li>
    <li>Why dental clinics should have a comprehensive understanding of sleep &amp; airway disorders, and educate their patients</li>
    <li>Overview of some of the latest technologies in dentistry and how each could be utilized in Dental Sleep Medicine (DSM)</li>
    <li>How to implement a sleep and airway management program in a dental clinic</li>
    <li>How to utilize your SOMNEx Plus System effectively in your clinic</li>
    <li>Proper selection of oral appliances for OSA</li>
  </ul>
</section>

</body>
</html>
```